Simple, elegant, business card design required

Hi designers,I am looking for a simple yet elegant business card design.

Please make use of my logo (attached); you are free to tweak the logo should you wish to do so.

Our business is involved in many different fields - almost all of them involved in some form of "design", so that's really one of the key things I want to portray. I do not wish to specify which field of design, exactly.

I prefer white on black (or just monochromatic), but if you have a different, creative idea, I am open to that too.

You can use artsy photographs provided that you have the license to use those. Please feel free to ask me any questions.
Updates

Project Deadline Extended Reason: Small extension for potential revisions. Did not get the time to provide as much feedback as I can. Added Wednesday, July 09, 2014

Target Market(s)

High-end customers looking for design consultancy

Industry/Entity Type

Business

Contact Information for Business Card

Name: Gareth Moonfield
Position: Creative Director
Mobile: +155603928174
Address: Barrow Lane, Ashcombe Vale, Thornshire GL12 4RT
Website: torvakest.com (not launched yet)

Requirements
Must have
• Design layout must be clean, original, and text must be readable when printed.
Should not have
• ~ No business card templates please. Anyone using this will be reported.
• ~ Please don't spam entries.

```html
<!DOCTYPE html>
<html lang="en">
<head>
<meta charset="utf-8">
<title>Gareth Moonfield – Business Card</title>
<link rel="stylesheet" href="https://fonts.googleapis.com/css2?family=Mulish:wght@400;500&display=swap">
<style>
  :root {
    --page-bg: #ffffff;
    --card-black: #000000;
    --panel-grey-light: #808082;
    --panel-grey-dark: #5a5a5c;
    --edge-light: #d4d5d7;
    --text-white: #ffffff;
    --accent-green: #a9c43c;
    --body-font: "Mulish", Arial, sans-serif;
  }
  html, body {
    margin: 0;
    padding: 0;
    width: 1200px;
    height: 1000px;
    overflow: hidden;
    background: var(--page-bg);
  }
  .business-card {
    position: absolute;
    left: 100px;
    top: 224px;
    width: 1000px;
    height: 552px;
    font-family: var(--body-font);
  }
  .card-artwork {
    position: absolute;
    inset: 0;
    display: block;
  }
  .identity {
    position: absolute;
    left: 98px;
    top: 88px;
  }
  .identity .person-name {
    margin: 0;
    font-size: 37px;
    font-weight: 400;
    line-height: 44px;
    color: var(--text-white);
  }
  .identity .job-title {
    margin: 0;
    font-size: 27px;
    font-weight: 400;
    line-height: 36px;
    color: var(--accent-green);
  }
  .contact-details {
    position: absolute;
    left: 98px;
    top: 338px;
    margin: 0;
    font-size: 23px;
    line-height: 30.5px;
    color: var(--text-white);
    font-style: normal;
  }
  .contact-details .label {
    color: var(--accent-green);
  }
  .brand {
    position: absolute;
    left: 634px;
    top: 245px;
    display: flex;
    align-items: center;
    gap: 40px;
  }
  .brand .brand-dot {
    width: 54px;
    height: 54px;
    border: 6px solid var(--text-white);
    border-radius: 50%;
    box-sizing: border-box;
  }
  .brand .brand-name {
    font-size: 27px;
    font-weight: 400;
    letter-spacing: 6px;
    color: var(--text-white);
  }
</style>
</head>
<body>
  <div class="business-card">
    <svg class="card-artwork" width="1000" height="552" viewBox="0 0 1000 552" aria-hidden="true">
      <defs>
        <linearGradient id="panel-grey" x1="0" y1="0" x2="0.3" y2="1">
          <stop offset="0" stop-color="var(--panel-grey-light)"/>
          <stop offset="1" stop-color="var(--panel-grey-dark)"/>
        </linearGradient>
        <linearGradient id="spine-grey" x1="0" y1="0" x2="0" y2="1">
          <stop offset="0" stop-color="#1a1a1a"/>
          <stop offset="0.6" stop-color="#3a3a3a"/>
          <stop offset="0.85" stop-color="#9a9b9d"/>
          <stop offset="1" stop-color="var(--edge-light)"/>
        </linearGradient>
        <linearGradient id="edge-glow" x1="0" y1="0" x2="0" y2="1">
          <stop offset="0" stop-color="#3a3a3a"/>
          <stop offset="0.5" stop-color="#8a8b8d"/>
          <stop offset="1" stop-color="var(--edge-light)"/>
        </linearGradient>
      </defs>
      <rect class="panel-grey" x="0" y="0" width="1000" height="552" fill="url(#panel-grey)"/>
      <path class="panel-curve" d="M585 380 Q 760 430 1000 330 L1000 552 L585 552 Z" fill="#000" opacity="0.06"/>
      <rect class="spine" x="0" y="0" width="28" height="552" fill="url(#spine-grey)"/>
      <polygon class="edge-strip" points="503,0 512,0 586,552 570,552" fill="url(#edge-glow)"/>
      <polygon class="panel-black" points="28,0 503,0 570,552 28,552" fill="var(--card-black)"/>
    </svg>

    <div class="identity">
      <h1 class="person-name">Gareth Moonfield</h1>
      <p class="job-title">Creative Director</p>
    </div>

    <address class="contact-details">
      <span class="label">Mobile</span>+155603928174<br>
      <span class="label">Address</span> Barrow Lane<br>
      Ashcombe Vale<br>
      Thornshire GL12 4RT<br>
      <span class="label">Website</span> torvakest.com
    </address>

    <div class="brand">
      <span class="brand-dot"></span>
      <span class="brand-name">TORVAKEST</span>
    </div>
  </div>
</body>
</html>
```